Automotive Accessories Business Card

Design a business template that match our new logo design and our industry.

https://www.kelvorauto.com/

Target Market(s)

Aftermarket auto parts and accessories

Industry/Entity Type

automotive

Contact Information for Business Card

company logo

Font styles to use
Serif
Sans Serif

Colors
EB3D1F
EC4F4E
F09395
F8D3D4
FCEDEE

```html
<!DOCTYPE html>
<html lang="en">
<head>
<meta charset="utf-8">
<title>Kelvor Auto Parts – Business Card</title>
<link rel="stylesheet" href="https://fonts.googleapis.com/css2?family=Arimo:wght@400;700&display=swap">
<style>
  :root {
    --red: #d3222f;
    --red-light: #e23a44;
    --charcoal: #333436;
    --card-dark: #2c2c2e;
    --card-dark-text: #3e3e41;
    --paper: #f4f4f4;
    --white: #ffffff;
    --backdrop: #e6e6e6;
    --muted: #b9b9bb;
  }
  * { margin: 0; padding: 0; box-sizing: border-box; }
  html, body {
    width: 1200px; height: 768px; overflow: hidden;
    background: var(--backdrop);
    font-family: "Arimo", Arial, sans-serif;
  }
  .stage { position: relative; width: 1200px; height: 768px; }
  .card {
    position: absolute; left: 300px; width: 600px; height: 343px;
    overflow: hidden; box-shadow: 0 6px 18px rgba(0,0,0,.18);
  }
  /* front */
  .card-front { top: 18px; background: var(--paper); }
  .contact-panel {
    position: absolute; left: 340px; top: 0; width: 260px; height: 343px;
    background: linear-gradient(160deg, var(--red-light), var(--red));
  }
  .brand {
    position: absolute; left: 40px; top: 118px; width: 280px;
    display: flex; align-items: center; gap: 10px;
  }
  .brand-square { flex: none; width: 18px; height: 18px; background: var(--red); }
  .brand-name {
    font-size: 22px; font-weight: 700; color: var(--charcoal);
    letter-spacing: .4px; white-space: nowrap;
  }
  .checker-block {
    position: absolute; left: 62px; top: 222px; width: 82px; height: 30px;
    background: var(--red);
  }
  .accent-band {
    position: absolute; left: 150px; top: 268px; width: 450px; height: 28px;
    background: var(--charcoal);
    clip-path: polygon(14px 0, 100% 0, 100% 100%, 0 100%);
  }
  .web-front {
    position: absolute; right: 30px; top: 275px;
    font-size: 14px; color: var(--white); letter-spacing: .3px;
  }
  .contact {
    position: absolute; left: 362px; top: 26px; width: 224px; color: var(--white);
    font-size: 12.5px; line-height: 1.32;
  }
  .person-name { font-size: 21px; font-weight: 700; letter-spacing: .6px; line-height: 1.1; }
  .person-role { margin-bottom: 8px; }
  .office { margin-bottom: 10px; }
  .phone { display: flex; align-items: center; gap: 6px; }
  .phone svg { width: 11px; height: 11px; fill: var(--white); }
  .email { margin-top: 2px; }
  /* back */
  .card-back { top: 407px; background: var(--card-dark); }
  .back-brand {
    position: absolute; left: 0; right: 0; top: 120px; text-align: center;
    font-size: 46px; font-weight: 700; color: var(--card-dark-text); letter-spacing: 1px;
  }
  .web-back {
    position: absolute; left: 0; right: 0; bottom: 46px; text-align: center;
    font-size: 13px; color: var(--muted); letter-spacing: 4px;
  }
</style>
</head>
<body>
<main class="stage">
  <section class="card card-front">
    <div class="contact-panel"></div>
    <div class="brand">
      <span class="brand-square"></span>
      <span class="brand-name">KELVOR AUTO PARTS</span>
    </div>
    <div class="checker-block" role="img" aria-label="Red and black checkered flag pattern"></div>
    <div class="accent-band"></div>
    <div class="web-front">www.kelvorauto.com</div>
    <div class="contact">
      <div class="person-name">DANIEL MERCER</div>
      <div class="person-role">Managing Director</div>
      <div class="office">
        240 W. Harbor Ave. Unit B<br>
        Fontana, CA, 92335<br>
        United States
        <div class="phone">
          <svg viewBox="0 0 24 24"><path d="M6.6 10.8a15.1 15.1 0 0 0 6.6 6.6l2.2-2.2a1 1 0 0 1 1-.25 11.4 11.4 0 0 0 3.6.57 1 1 0 0 1 1 1V20a1 1 0 0 1-1 1A17 17 0 0 1 3 4a1 1 0 0 1 1-1h3.5a1 1 0 0 1 1 1c0 1.25.2 2.45.57 3.57a1 1 0 0 1-.25 1z"/></svg>
          1-800-555-0142
        </div>
      </div>
      <div class="office">
        5120 Fraser Lane<br>
        Burnaby, BC V5H 2K4<br>
        Canada
        <div class="phone">
          <svg viewBox="0 0 24 24"><path d="M6.6 10.8a15.1 15.1 0 0 0 6.6 6.6l2.2-2.2a1 1 0 0 1 1-.25 11.4 11.4 0 0 0 3.6.57 1 1 0 0 1 1 1V20a1 1 0 0 1-1 1A17 17 0 0 1 3 4a1 1 0 0 1 1-1h3.5a1 1 0 0 1 1 1c0 1.25.2 2.45.57 3.57a1 1 0 0 1-.25 1z"/></svg>
          604-555-0187
        </div>
      </div>
      <div class="email">sales@kelvorauto.com</div>
    </div>
  </section>

  <section class="card card-back">
    <div class="back-brand">KELVOR AUTO PARTS</div>
    <div class="web-back">www.kelvorauto.com</div>
  </section>
</main>
</body>
</html>
```